Wavelink Earphone Packaging Design

We want to use the packaging for 4-5 of our Wavelink Earphone series (Picture enclosed) and hence we would not like to put any product pictures on the packaging.

Material: E-Flute Paper box
Type: Window Box style
Design features we prefer: Colorful, creative, trendy, High tech.
Requirement: AI file is preferred
Size of Packaging: (L) 95 x (W) 40 x (H) 120 mm

Enclosed are a detailed description along with competitor designs for your reference.

Any further questions, please feel free to ask

```html
<!DOCTYPE html>
<html lang="en">
<head>
<meta charset="utf-8">
<title>Wavelink Earphone 5.0 – Window Box Front</title>
<link rel="stylesheet" href="https://fonts.googleapis.com/css2?family=Rajdhani:wght@500;600;700&display=swap">
<style>
  :root {
    --bg: #e9e9ea;
    --panel: #29223d;
    --panel-dark: #231d35;
    --accent-blue: #2a9fe0;
    --window-fill: #f4f4f5;
    --brand-text: #ffffff;
  }
  html, body {
    margin: 0;
    padding: 0;
    width: 1200px;
    height: 885px;
    overflow: hidden;
    background: var(--bg);
    font-family: "Rajdhani", sans-serif;
  }
  .canvas {
    position: relative;
    width: 1200px;
    height: 885px;
  }
  .hang-tab {
    position: absolute;
    left: 328px;
    top: 15px;
    width: 544px;
    height: 118px;
    background: var(--panel-dark);
  }
  .hang-hole {
    position: absolute;
    left: 162px;
    top: 45px;
    width: 156px;
    height: 26px;
    border-radius: 13px;
    background: var(--bg);
  }
  .front-panel {
    position: absolute;
    left: 332px;
    top: 130px;
    width: 536px;
    height: 735px;
    background: var(--panel);
    overflow: hidden;
  }
  .brand {
    position: absolute;
    left: 20px;
    top: 47px;
    display: flex;
    align-items: center;
    gap: 6px;
    color: var(--brand-text);
    font-weight: 700;
    font-size: 20px;
    letter-spacing: 0.2px;
  }
  .brand-dot {
    width: 16px;
    height: 16px;
    border-radius: 50%;
    background: var(--accent-blue);
  }
  .product-window {
    position: absolute;
    left: 160px;
    top: 55px;
    width: 372px;
    height: 392px;
  }
  .product-name {
    position: absolute;
    left: 72px;
    top: 370px;
    writing-mode: vertical-rl;
    color: var(--accent-blue);
    font-weight: 500;
    font-size: 27px;
    letter-spacing: 1px;
    white-space: nowrap;
  }
  .version {
    position: absolute;
    left: 78px;
    top: 630px;
  }
  .color-burst {
    position: absolute;
    left: 260px;
    top: 440px;
  }
</style>
</head>
<body>
<div class="canvas">
  <div class="hang-tab">
    <div class="hang-hole"></div>
  </div>

  <div class="front-panel">
    <div class="brand"><span class="brand-dot"></span>Wavelink</div>

    <svg class="product-window" viewBox="0 0 372 392" role="img" aria-label="Product window showing the wireless earphones with lime green cable">
      <path d="M60 6 H348 Q366 6 366 24 V290 Q366 386 270 386 H24 Q6 386 6 368 V60 Q6 6 60 6 Z"
            fill="var(--window-fill)" stroke="var(--accent-blue)" stroke-width="9"/>
    </svg>

    <div class="product-name">Wavelink Earphone</div>

    <svg class="version" width="90" height="70" viewBox="0 0 90 70">
      <defs>
        <linearGradient id="versionGradient" x1="0" y1="0" x2="1" y2="1">
          <stop offset="0" stop-color="#f2c14e"/>
          <stop offset="0.5" stop-color="#e86fa8"/>
          <stop offset="1" stop-color="#6a8cf0"/>
        </linearGradient>
      </defs>
      <text x="2" y="58" font-family="Rajdhani, sans-serif" font-weight="600" font-size="64"
            fill="none" stroke="url(#versionGradient)" stroke-width="1.6">5.0</text>
    </svg>

    <svg class="color-burst" width="276" height="295" viewBox="0 0 276 295" role="img" aria-label="Colourful diagonal streak decoration in green, teal, purple, pink and orange">
      <defs>
        <linearGradient id="burstGradient" x1="0" y1="0" x2="1" y2="1">
          <stop offset="0" stop-color="#8fd36a"/>
          <stop offset="0.35" stop-color="#3fc6c9"/>
          <stop offset="0.6" stop-color="#9a6ee0"/>
          <stop offset="0.8" stop-color="#e25fb4"/>
          <stop offset="1" stop-color="#f6a23c"/>
        </linearGradient>
      </defs>
      <path d="M150 0 L276 40 L276 250 L200 295 L60 295 L0 230 Z" fill="url(#burstGradient)" opacity="0.9"/>
    </svg>
  </div>
</div>
</body>
</html>
```